Business card design needed for Pollen Bakes

We need a new business card designed for our business. We create complete DIY cake kits to be delivered Australia Wide.

I would like our logo used (see attached).

Industry/Entity Type

Business

Contact Information for Business Card

Pollen Bakes - Complete DIY Cake Kits
www.pollenbakes.com.au
0472 315 904
sales@pollenbakes.com.au
www.facebook.com/pollenbakes1

Requirements
Must have
• logo

```html
<!DOCTYPE html>
<html lang="en">
<head>
<meta charset="utf-8">
<title>Pollen Bakes – Business Card</title>
<link href="https://fonts.googleapis.com/css2?family=Roboto+Condensed:wght@400;700&display=swap" rel="stylesheet">
<style>
  :root {
    --stage: #2c2c2e;
    --pink-light: #f0c6d1;
    --pink-deep: #d38aa0;
    --card-white: #fdf4f6;
    --brand-red: #c01a2e;
    --teal: #3b8c88;
    --text-grey: #555257;
    --divider: #d9cfd2;
    --art-pink: #e99ab3;
    --art-brown: #9a6a45;
  }
  * { box-sizing: border-box; margin: 0; padding: 0; }
  html, body {
    width: 1200px; height: 900px; overflow: hidden;
    background: var(--stage);
    font-family: "Roboto Condensed", Arial, sans-serif;
  }
  .stage {
    width: 1200px; height: 900px;
    display: flex; align-items: center; justify-content: center; gap: 40px;
  }
  .card {
    width: 525px; height: 300px; position: relative; overflow: hidden;
    box-shadow: 0 10px 30px rgba(0,0,0,.45);
  }
  .card-front {
    background: radial-gradient(ellipse at 50% 45%, var(--pink-light) 0%, var(--pink-deep) 100%);
    display: flex; flex-direction: column; align-items: center; justify-content: center; gap: 14px;
  }
  .brand-art {
    width: 150px; height: 120px; border-radius: 60px 60px 18px 18px;
    background: linear-gradient(160deg, var(--art-pink) 0%, var(--art-brown) 100%);
    opacity: .85;
  }
  .brand-lockup { display: flex; align-items: center; gap: 10px; }
  .brand-dot { width: 16px; height: 16px; border-radius: 50%; background: var(--brand-red); }
  .brand-name {
    font-weight: 700; font-size: 40px; color: var(--brand-red); line-height: 1; white-space: nowrap;
  }
  .card-back { background: var(--card-white); display: flex; }
  .back-logo {
    width: 215px; flex: none; display: flex; flex-direction: column; align-items: center; justify-content: center; gap: 10px;
  }
  .back-logo .brand-art { width: 110px; height: 90px; }
  .back-logo .brand-name { font-size: 26px; }
  .back-logo .brand-dot { width: 11px; height: 11px; }
  .divider { width: 1px; flex: none; margin: 40px 0; background: var(--divider); }
  .contact { padding: 48px 0 0 34px; }
  .person-name { font-size: 30px; color: var(--teal); font-weight: 400; margin-bottom: 18px; white-space: nowrap; }
  .contact-list { list-style: none; }
  .contact-list li {
    display: flex; align-items: center; gap: 12px;
    font-size: 16px; color: var(--text-grey); margin-bottom: 7px; white-space: nowrap;
  }
  .contact-list svg { width: 14px; height: 14px; flex: none; }
</style>
</head>
<body>
<main class="stage">
  <section class="card card-front" aria-label="Business card front">
    <div class="brand-art" role="img" aria-label="Illustration of a baker holding a piping bag and a pink cupcake"></div>
    <div class="brand-lockup">
      <span class="brand-dot"></span>
      <span class="brand-name">Pollen Bakes</span>
    </div>
  </section>

  <section class="card card-back" aria-label="Business card back">
    <div class="back-logo">
      <div class="brand-art" role="img" aria-label="Illustration of a baker holding a piping bag and a pink cupcake"></div>
      <div class="brand-lockup">
        <span class="brand-dot"></span>
        <span class="brand-name">Pollen Bakes</span>
      </div>
    </div>
    <div class="divider"></div>
    <div class="contact">
      <h1 class="person-name">Tessa Marlow</h1>
      <ul class="contact-list">
        <li>
          <svg viewBox="0 0 16 16" fill="#3b8c88" aria-hidden="true"><path d="M3.5 1.5l2.5 0 1 3.5-1.6 1.2a8 8 0 0 0 4.4 4.4L11 9l3.5 1v2.5c0 1-1 2-2 2A11 11 0 0 1 1.5 3.5c0-1 1-2 2-2z"/></svg>
          0472 315 904
        </li>
        <li>
          <svg viewBox="0 0 16 16" fill="none" stroke="#3b8c88" stroke-width="1.6" aria-hidden="true"><rect x="1.5" y="3.5" width="13" height="9" rx="1"/><path d="M1.5 4l6.5 5 6.5-5"/></svg>
          sales@pollenbakes.com.au
        </li>
        <li>
          <svg viewBox="0 0 16 16" fill="none" stroke="#3b8c88" stroke-width="1.4" aria-hidden="true"><circle cx="8" cy="8" r="6.5"/><ellipse cx="8" cy="8" rx="3" ry="6.5"/><path d="M1.5 8h13"/></svg>
          www.pollenbakes.com.au
        </li>
        <li>
          <svg viewBox="0 0 16 16" aria-hidden="true"><rect x="1.5" y="1.5" width="13" height="13" rx="2" fill="#3b8c88"/></svg>
          www.socialpage.net/pollenbakes1
        </li>
      </ul>
    </div>
  </section>
</main>
</body>
</html>
```